Garlic Farm for Farm Sales/Restaurant sales

Need a professional, but appealing to agriculture world. We are selling 27 kinds of Organic Garlic from a farm in Simla,CO. I have uploaded logo and business information-we are going to need a template, because I will need to use it for four separate people.
-We are trying to appeal to Farm to table restaurants
-As well as growers/farmers

Target Market(s)

Agriculture Sales/Restaurants-Organic

Industry/Entity Type

Agriculture

Contact Information for Business Card

Want it to look more unique then your average brimly ink card- I want it to look amazing

Font styles to use
Sans Serif

Colors
0455a3
ec1f27
fbed22
ffffff

Requirements
Must have
• Just be creative
Nice to have
• Colorful
Should not have
• plain

```html
<!DOCTYPE html>
<html lang="en">
<head>
<meta charset="utf-8">
<title>Ridgeline Garlic – Business Card</title>
<link rel="stylesheet" href="https://fonts.googleapis.com/css2?family=Source+Sans+3:wght@400;600;700&display=swap">
<style>
  :root {
    --stage: #1c1c1c;
    --card-front: #ffffff;
    --card-back: #f4f4f4;
    --brand-red: #bd0b2c;
    --brand-navy: #12285a;
    --text-grey: #3a3a3a;
  }
  * { box-sizing: border-box; margin: 0; padding: 0; }
  html, body {
    width: 1200px; height: 900px; overflow: hidden;
    background: var(--stage);
    font-family: "Source Sans 3", "Myriad Pro", Arial, sans-serif;
  }
  .stage { position: relative; width: 1200px; height: 900px; }
  .card {
    position: absolute; top: 170px; width: 347px; height: 561px;
    text-align: center;
  }
  .card--front { left: 259px; background: var(--card-front); }
  .card--back { left: 631px; background: var(--card-back); }

  .band {
    position: absolute; left: 102px; width: 143px; height: 30px;
    background: var(--brand-red);
  }
  .band--top { top: 0; }
  .band--bottom { bottom: 0; height: 28px; }

  .brand-mark {
    position: absolute; left: 0; right: 0;
    display: flex; flex-direction: column; align-items: center; gap: 14px;
  }
  .card--front .brand-mark { top: 98px; }
  .card--back .brand-mark { top: 185px; }
  .brand-dot { border-radius: 50%; background: var(--brand-red); }
  .card--front .brand-dot { width: 130px; height: 130px; }
  .card--back .brand-dot { width: 110px; height: 110px; }
  .brand-name {
    font-weight: 700; color: var(--brand-navy); letter-spacing: 0.5px;
  }
  .card--front .brand-name { display: none; }
  .card--back .brand-name { font-size: 38px; line-height: 1; }

  .person { position: absolute; top: 294px; left: 0; right: 0; }
  .person__name {
    font-size: 23px; font-weight: 600; color: var(--brand-red);
    text-transform: uppercase; letter-spacing: 0.2px;
  }
  .person__role { font-size: 15px; color: var(--text-grey); margin-top: 3px; }

  .contact { position: absolute; top: 362px; left: 0; right: 0; font-size: 15px; color: var(--text-grey); line-height: 21px; }
  .contact__label { color: var(--brand-red); font-weight: 700; }
  .address { position: absolute; top: 446px; left: 0; right: 0; font-size: 15px; color: var(--text-grey); line-height: 18px; }

  .website {
    position: absolute; top: 474px; left: 0; right: 0;
    font-size: 16px; color: var(--brand-red);
  }
</style>
</head>
<body>
<main class="stage">
  <section class="card card--front" aria-label="Business card front">
    <div class="band band--top"></div>
    <div class="brand-mark">
      <span class="brand-dot"></span>
      <span class="brand-name">Ridgeline Garlic</span>
    </div>
    <div class="person">
      <h1 class="person__name">Aaron Pell</h1>
      <p class="person__role">Managing Director</p>
    </div>
    <div class="contact">
      <p><span class="contact__label">P:</span> 555-014-2290</p>
      <p><span class="contact__label">F:</span> 555-014-2290</p>
      <p><span class="contact__label">E:</span> hello@ridgelinegarlic.com</p>
    </div>
    <div class="address">
      <p>1234, Address Goes Here</p>
      <p>Country Name, 123456</p>
    </div>
    <div class="band band--bottom"></div>
  </section>

  <section class="card card--back" aria-label="Business card back">
    <div class="brand-mark">
      <span class="brand-dot"></span>
      <span class="brand-name">Ridgeline Garlic</span>
    </div>
    <p class="website">www.ridgelinegarlic.com</p>
  </section>
</main>
</body>
</html>
```